Homepage design for female-owned English/French speaking Law firm

Brief Update - we prefer not to have a photo of a person in the hero shot

Corvell.com.au is the website for a English/French Bilingual Female-owned Law Firm, Morillaqua Corvell.
Overall Design notes:
Professional, yet warm and welcoming
Historic foundations but Progressive, woman-owned, sleek, innovative and modern.
Approachable, casual yet professional. Sans-serif font and light colours would help this
2 languages switched by flags (English/French)

Winner must provide
Home page design
Standard (inner) page design (can be provided after winner is selected)
All photos used in the design without charge
Updates

Requirements
Should not have
• Update - we prefer not to have a photo of a person in the hero shot

```html
<!DOCTYPE html>
<html lang="en">
<head>
<meta charset="utf-8">
<title>Morillaqua Corvell – French-Speaking Lawyers</title>
<link rel="stylesheet" href="https://fonts.googleapis.com/css2?family=Inter:wght@400;500;600;700&display=swap">
<style>
:root{
  --orange:#fd8f2a;
  --navy:#08496a;
  --ink:#2f3438;
  --muted:#5b6066;
  --grey-icon:#7d8185;
  --page:#f0f3f6;
  --white:#ffffff;
  --line:#c9cfd5;
}
*{box-sizing:border-box;margin:0;padding:0}
html,body{width:1200px;height:3225px;overflow:hidden}
body{position:relative;background:var(--page);font-family:'Inter',sans-serif;color:var(--ink)}
.abs{position:absolute}

/* hero */
.hero-photo{position:absolute;left:0;top:0;width:1200px;height:800px;
  background:linear-gradient(180deg,#c9d4dc 0%,#98adbb 25%,#6f8ea3 50%,#3f6a85 72%,#0d4a6a 90%,#f0f3f6 100%)}
.topbar{top:12px;left:66px;right:66px;display:flex;align-items:center;gap:18px;font-size:11px;color:#3c4247}
.topbar span{display:flex;align-items:center;gap:8px}
.lang{position:absolute;right:66px;top:8px;display:flex;align-items:center;gap:6px}
.brand{left:66px;top:58px;font-size:22px;font-weight:400;color:var(--orange);letter-spacing:-.3px;line-height:1}
.brand small{display:block;font-size:8.5px;letter-spacing:1.8px;margin-top:4px;color:var(--orange)}
.nav{top:73px;left:599px;display:flex;gap:27px;font-size:13.5px;font-weight:500;color:#343a40}
.nav a{text-decoration:none;color:inherit;padding-bottom:6px}
.nav .active{color:var(--orange);border-bottom:2px solid var(--orange)}
.btn{display:flex;align-items:center;justify-content:center;font-size:13.5px;font-weight:600;color:var(--white);background:var(--orange)}
.btn-contact{left:995px;top:56px;width:138px;height:42px}
.hero-title{left:66px;top:166px;font-size:70px;font-weight:500;line-height:76px;color:var(--white);letter-spacing:-.5px}
.hero-text{left:66px;top:421px;width:600px;font-size:14px;line-height:22px;color:var(--white)}
.btn-appt{left:66px;top:513px;width:200px;height:41px}
.btn-ghost{left:294px;top:513px;width:199px;height:41px;background:transparent;border:1.5px solid var(--white)}

/* services */
.h2{font-size:44px;font-weight:500;color:var(--ink);letter-spacing:-.3px}
.services-title{left:66px;top:842px}
.services-text{left:66px;top:905px;width:440px;font-size:14px;line-height:21px;color:var(--muted)}
.card{position:absolute;width:254px;height:199px;background:var(--white);display:flex;flex-direction:column;align-items:center;justify-content:center;text-align:center;font-size:13.5px;font-weight:500;line-height:16px;color:var(--grey-icon)}
.card svg{width:58px;height:58px;margin-bottom:18px;stroke:var(--grey-icon);fill:none;stroke-width:2}
.card.featured{background:var(--orange);color:var(--white)}
.card.featured svg{stroke:var(--white)}

/* stats */
.stats{left:0;top:1471px;width:1200px;height:157px;background:var(--navy);display:flex;justify-content:center;align-items:center}
.stat{width:243px;text-align:center;color:var(--white)}
.stat+.stat{border-left:1.5px solid #5f8aa3}
.stat p{font-size:13.5px;font-weight:500}
.stat strong{display:block;font-size:44px;font-weight:600;margin-top:12px;line-height:1}

/* about */
.about-photo{left:0;top:1628px;width:1200px;height:483px;
  background:radial-gradient(ellipse at 50% 30%,#a9bac6 0%,#7d97a9 35%,#3c6683 70%,#134d6c 100%)}
.about-title{left:0;top:1700px;width:1200px;text-align:center;color:var(--white)}
.about-list{left:245px;top:1793px;width:710px;list-style:none;text-align:center;color:var(--white);font-size:13.5px;line-height:21px}
.about-list li{margin-bottom:21px}
.about-list li::before{content:"•";margin-right:7px}
.btn-about{left:492px;top:1975px;width:199px;height:41px}

/* contact */
.touch-title{left:66px;top:2210px;width:468px;text-align:center}
.touch-sub{left:66px;top:2272px;width:468px;text-align:center;font-size:14px;line-height:21px;color:var(--ink)}
.address{left:66px;top:2383px;font-size:14px;line-height:27px}
.contact-lines{left:350px;top:2378px;font-size:14px;line-height:31px}
.contact-lines div{display:flex;align-items:center;gap:10px}
.field-label{position:absolute;left:642px;font-size:13.5px;font-weight:600}
.field-label b{color:#e0242b;font-weight:600}
.field{position:absolute;left:642px;width:450px;height:42px;background:var(--white);border:1.5px solid var(--line);border-radius:4px;font-size:13.5px;color:#8b9197;padding:13px 16px}
.btn-send{left:642px;top:2642px;width:200px;height:42px}

/* footer */
.footer{left:0;top:2760px;width:1200px;height:465px;background:var(--navy);color:var(--white)}
.footer .brand-foot{position:absolute;left:66px;top:62px;font-size:28px;color:var(--orange);line-height:1}
.footer .brand-foot small{display:block;font-size:9.5px;letter-spacing:2.4px;margin-top:6px}
.footer .blurb{position:absolute;left:66px;top:161px;width:340px;font-size:13.5px;line-height:21px}
.fcol{position:absolute;top:75px;font-size:13px;font-weight:600}
.fcol h4{font-size:16px;font-weight:600;margin-bottom:16px}
.fcol p{margin-bottom:19px;line-height:16px}
.copy{position:absolute;left:66px;top:418px;font-size:11px}
</style>
</head>
<body>

<div class="hero-photo" role="img" aria-label="Misty harbour view with the Sydney Opera House and Harbour Bridge in blue tones"></div>

<div class="abs topbar">
  <span><svg width="11" height="9" viewBox="0 0 11 9"><rect x="0.5" y="0.5" width="10" height="8" fill="none" stroke="#3c4247"/><path d="M0.5 0.5 5.5 5 10.5 0.5" fill="none" stroke="#3c4247"/></svg>hello@corvell.com.au</span>
  <span><svg width="11" height="11" viewBox="0 0 24 24"><path d="M6.6 10.8a15 15 0 0 0 6.6 6.6l2.2-2.2c.3-.3.7-.4 1-.2 1.1.4 2.3.6 3.6.6.6 0 1 .4 1 1V20c0 .6-.4 1-1 1A17 17 0 0 1 3 4c0-.6.4-1 1-1h3.5c.6 0 1 .4 1 1 0 1.3.2 2.5.6 3.6.1.3 0 .7-.2 1z" fill="#3c4247"/></svg>(+612) 9400 2150</span>
  <span><svg width="11" height="11" viewBox="0 0 24 24"><circle cx="12" cy="12" r="4" fill="none" stroke="#3c4247" stroke-width="2.5"/><path d="M12 2v4M12 18v4M2 12h4M18 12h4M5 5l3 3M16 16l3 3M5 19l3-3M16 8l3-3" stroke="#3c4247" stroke-width="2.5"/></svg>Migration Agent’s registration No : 1048275</span>
  <div class="lang"><svg width="27" height="18" viewBox="0 0 27 18"><rect width="9" height="18" fill="#1d3fb8"/><rect x="9" width="9" height="18" fill="#fff"/><rect x="18" width="9" height="18" fill="#e52a2a"/></svg><svg width="11" height="7" viewBox="0 0 11 7"><path d="M1 1l4.5 4.5L10 1" fill="none" stroke="#333" stroke-width="1.5"/></svg></div>
</div>

<div class="abs brand">morillaqua corvell solicitors<small>French Speaking Lawyers</small></div>

<nav class="abs nav">
  <a class="active">Home</a><a>About us</a><a>Our service ⌄</a><a>Download &amp; Link</a>
</nav>
<div class="abs btn btn-contact">Contact us</div>

<h1 class="abs hero-title">WE ARE A FIRM OF<br>FRENCH-SPEAKING<br>LAWYERS</h1>
<p class="abs hero-text">located in the Sydney central business district. We provide a broad range of legal services in English and French to clients in Australia and overseas.</p>
<div class="abs btn btn-appt">Appointment now</div>
<div class="abs btn btn-ghost">Lean more</div>

<h2 class="abs h2 services-title">OUR SERVICES</h2>
<p class="abs services-text">If you have a question relating to other areas of law, please do not hesitate to contact us for referral to an expert in the relevant field.</p>

<div class="card featured" style="left:66px;top:995px"><svg viewBox="0 0 58 58"><path d="M6 26 29 10l23 16M11 23v29h36V23M18 52V34h8v18M32 34h10v10H32zM10 8h22v6"/></svg>Property Law including<br>Conveyancing &amp; Leases.</div>
<div class="card" style="left:338px;top:995px"><svg viewBox="0 0 58 58"><rect x="6" y="17" width="46" height="32"/><path d="M22 17v-6h14v6M6 30h46M25 27h8v6h-8z"/></svg>Sale &amp; Purchase of<br>Business.</div>
<div class="card" style="left:608px;top:995px"><svg viewBox="0 0 58 58"><path d="M14 5h22l10 10v38H14zM36 5v10h10M20 36h20M20 42h14"/></svg>Deceased Estates &amp;<br>Wills.</div>
<div class="card" style="left:880px;top:995px"><svg viewBox="0 0 58 58"><path d="M4 14l22-6v44L4 46zM30 8l24 6v32l-24 6zM10 22h12M16 20v4M12 32l6-6M36 40l6-18 6 18M38 34h8"/></svg>Translation service.</div>

<div class="card" style="left:66px;top:1210px"><svg viewBox="0 0 58 58"><path d="M4 8h34v22H18l-8 7v-7H4zM44 20h10v22h-6v7l-8-7H22v-8M10 15h22M10 21h22"/></svg>Advice in relation to<br>transactions in France.</div>
<div class="card" style="left:338px;top:1210px"><svg viewBox="0 0 58 58"><path d="M6 6v46h48M12 40l8-16 8 10 8-14 8 8 6-6M12 46l10-8 8 4 10-10 12 4"/></svg>Affairs Management.</div>
<div class="card" style="left:608px;top:1210px"><svg viewBox="0 0 58 58"><circle cx="28" cy="10" r="5"/><path d="M24 18h8l2 14h-3v20h-8V32h-3zM36 28v24"/></svg>Elder Law.</div>
<div class="card" style="left:880px;top:1210px"><svg viewBox="0 0 58 58"><circle cx="20" cy="8" r="5"/><path d="M16 16h8v36h-8zM24 24h16M40 20v18M32 32l4 8h8l4-8M34 32h12"/></svg>Powers of Attorney /<br>Guardianship.</div>

<section class="abs stats">
  <div class="stat"><p>Founded in</p><strong>1930s</strong></div>
  <div class="stat"><p>Trusted customer</p><strong>5000+</strong></div>
  <div class="stat"><p>Successful Case</p><strong>4560+</strong></div>
  <div class="stat"><p>Case Closed</p><strong>3500+</strong></div>
</section>

<div class="abs about-photo" role="img" aria-label="Soft blue view of the Sydney Opera House sails at dusk"></div>
<h2 class="abs h2 about-title">ABOUT US</h2>
<ul class="abs about-list">
  <li>Our small, skilled team is committed to the delivery of quality legal services to our clients.</li>
  <li>Morillaqua Corvell originated with the legal practice founded by Mr Lucien Marcel Morillaqua in the 1930s. Today, we are a progressive law firm that has embraced both the traditional approach of our predecessor firms and the efficiencies of modern technology.</li>
  <li>All of our services are available in English or in French according to the needs of our clients.</li>
</ul>
<div class="abs btn btn-about">Learn more</div>

<h2 class="abs h2 touch-title">GET IN TOUCH</h2>
<p class="abs touch-sub">Looking for good lawyer? , Don’t be shy.<br>Let’s work together.</p>
<div class="abs address">Level 9, 48 Harbour street<br>Sydney, NSW 2000<br>Australia</div>
<div class="abs contact-lines">
  <div><svg width="11" height="11" viewBox="0 0 24 24"><path d="M6.6 10.8a15 15 0 0 0 6.6 6.6l2.2-2.2c.3-.3.7-.4 1-.2 1.1.4 2.3.6 3.6.6.6 0 1 .4 1 1V20c0 .6-.4 1-1 1A17 17 0 0 1 3 4c0-.6.4-1 1-1h3.5c.6 0 1 .4 1 1 0 1.3.2 2.5.6 3.6.1.3 0 .7-.2 1z" fill="#2f3438"/></svg>Phone: (+612) 9400 2150</div>
  <div><svg width="11" height="11" viewBox="0 0 11 11"><rect x="1" y="3" width="9" height="7" fill="#2f3438"/><rect x="3" y="0.5" width="5" height="3" fill="none" stroke="#2f3438"/></svg>Fax: (+612) 9400 2151</div>
  <div><svg width="11" height="9" viewBox="0 0 11 9"><rect width="11" height="9" fill="#2f3438"/><path d="M0.5 0.8 5.5 5 10.5 0.8" fill="none" stroke="#fff"/></svg>E-mail: hello@corvell.com.au</div>
</div>

<label class="field-label" style="top:2187px">Full name <b>*</b></label>
<div class="field" style="top:2216px">Full name</div>
<label class="field-label" style="top:2269px">Email <b>*</b></label>
<div class="field" style="top:2298px">Youremail@address.com</div>
<label class="field-label" style="top:2351px">Phone number</label>
<div class="field" style="top:2380px;width:310px">Phone number</div>
<label class="field-label" style="top:2433px">Message <b>*</b></label>
<div class="field" style="top:2461px;height:153px">How we can help you?</div>
<div class="abs btn btn-send">Send</div>

<footer class="abs footer">
  <div class="brand-foot">morillaqua corvell solicitors<small>French Speaking Lawyers</small></div>
  <p class="blurb">Lorem ipsum dolor sit amet consectetur. Elit vitae fringilla quisque dictum cras urna lacus tristique et.</p>
  <div class="fcol" style="left:518px"><h4>Get to know us</h4><p>Home</p><p>About us</p><p>Download &amp; Link</p></div>
  <div class="fcol" style="left:698px"><h4>Our service</h4><p>Property law</p><p>Sale of Business</p><p>Wills &amp; Estates</p><p>Translation</p><p>Elder Law</p><p>Powers of Attorney</p><p>French advice</p><p>Affairs management</p></div>
  <div class="fcol" style="left:880px;width:260px"><h4>Contact us</h4><p>Level 9, 48 Harbour street<br>Sydney, NSW 2000<br>Australia</p><p>Phone: (+612) 9400 2150</p><p>Fax: (+612) 9400 2151</p><p>E-mail: hello@corvell.com.au</p></div>
  <p class="copy">2024 © Copyright, morillaqua corvell. All rights reserved.</p>
</footer>

</body>
</html>
```